Design a Shirt Hang Tag for a brand new streetwear company

We need a hang tag for our apparel. This will be attached and shipper with every shirt, hat, and hoodie. We make streetwear/urban apparel. For a feel of our products see http://loomferal.co

We'd like to see something die cut with a shape that isn't a rectangle.
Looking for a design that embodies "Savage". We are looking for something bold and fun. Our colors usually consist of black. white, and red, but if you feel like doing something else that you feel could fit our brand,go for it. Were savage, we don't want normal.

Target Market(s)

inner city, age 13-29, multi-cultural

Industry/Entity Type

Clothing

Font styles to use
Sans Serif
Other font styles liked:
• artist's choice

Colors
ec1f27
ffffff
000000

Requirements
Must have
• site url: www.loomferal.co
• Band Name: Loom Feral
• Double sided tag
• Die cut design

```html
<!DOCTYPE html>
<html lang="en">
<head>
<meta charset="utf-8">
<title>Loom Feral — Hang Tag, Front and Back</title>
<link rel="stylesheet" href="https://fonts.googleapis.com/css2?family=Barlow+Condensed:wght@600&family=Barlow:wght@600&display=swap">
<style>
  :root {
    --tag-black: #000000;
    --brand-red: #ec1f27;
    --paper-white: #ffffff;
    --pattern-red: #9a141a;
  }
  * { margin: 0; padding: 0; box-sizing: border-box; }
  html, body { width: 1200px; height: 1200px; overflow: hidden; background: var(--paper-white); }
  .sheet { position: relative; width: 1200px; height: 1200px; }
  .hang-tag { position: absolute; top: 85px; width: 202px; height: 385px; overflow: visible; }
  .hang-tag--front { left: 243px; }
  .hang-tag--back { left: 798px; }
  .tag-body { fill: var(--tag-black); }
  .slash-line { stroke: var(--brand-red); stroke-width: 2; }
  .slash-bar { fill: var(--brand-red); }
  .squiggle-field { fill: var(--pattern-red); }
  .brand-name {
    font-family: "Barlow Condensed", sans-serif;
    font-weight: 600;
    font-size: 34px;
    fill: var(--paper-white);
  }
  .site-url {
    font-family: "Barlow", sans-serif;
    font-weight: 600;
    font-size: 23px;
    fill: var(--paper-white);
  }
</style>
</head>
<body>
<main class="sheet">

  <svg class="hang-tag hang-tag--front" viewBox="0 0 202 385" aria-label="Hang tag front">
    <defs>
      <clipPath id="front-cut">
        <path d="M75,0 H120 L125,42 Q140,44 145,50 Q187,55 190,85 L188,115 L188,340 Q202,350 202,368 Q202,385 185,385 H15 Q0,385 0,368 Q0,350 12,340 L12,115 Q0,105 0,85 Q3,55 57,50 Q62,44 72,42 Z"/>
      </clipPath>
    </defs>
    <path class="tag-body" d="M75,0 H120 L125,42 Q140,44 145,50 Q187,55 190,85 L188,115 L188,340 Q202,350 202,368 Q202,385 185,385 H15 Q0,385 0,368 Q0,350 12,340 L12,115 Q0,105 0,85 Q3,55 57,50 Q62,44 72,42 Z"/>
    <g clip-path="url(#front-cut)">
      <g transform="rotate(-33 101 200)">
        <line class="slash-line" x1="-100" y1="110" x2="300" y2="110"/>
        <line class="slash-line" x1="-100" y1="170" x2="300" y2="170"/>
        <line class="slash-line" x1="-100" y1="230" x2="300" y2="230"/>
        <line class="slash-line" x1="-100" y1="290" x2="300" y2="290"/>
        <line class="slash-line" x1="-100" y1="350" x2="300" y2="350"/>
        <rect class="slash-bar" x="0" y="160" width="120" height="11"/>
        <rect class="slash-bar" x="40" y="182" width="130" height="11"/>
        <rect class="slash-bar" x="20" y="208" width="140" height="11"/>
        <rect class="slash-bar" x="60" y="232" width="120" height="11"/>
        <rect class="slash-bar" x="40" y="256" width="130" height="11"/>
      </g>
    </g>
    <rect class="squiggle-field" x="8" y="70" width="44" height="45" role="img" aria-label="Red wavy line pattern"/>
    <rect class="squiggle-field" x="142" y="290" width="46" height="45" role="img" aria-label="Red wavy line pattern"/>
    <text class="brand-name" transform="translate(97 320) rotate(-90)" dominant-baseline="central" textLength="222" lengthAdjust="spacing">LOOM FERAL</text>
  </svg>

  <svg class="hang-tag hang-tag--back" viewBox="0 0 202 385" aria-label="Hang tag back">
    <defs>
      <clipPath id="back-cut">
        <path d="M75,0 H120 L125,42 Q140,44 145,50 Q187,55 190,85 L188,115 L188,340 Q202,350 202,368 Q202,385 185,385 H15 Q0,385 0,368 Q0,350 12,340 L12,115 Q0,105 0,85 Q3,55 57,50 Q62,44 72,42 Z"/>
      </clipPath>
    </defs>
    <path class="tag-body" d="M75,0 H120 L125,42 Q140,44 145,50 Q187,55 190,85 L188,115 L188,340 Q202,350 202,368 Q202,385 185,385 H15 Q0,385 0,368 Q0,350 12,340 L12,115 Q0,105 0,85 Q3,55 57,50 Q62,44 72,42 Z"/>
    <g clip-path="url(#back-cut)">
      <g transform="rotate(-33 101 200)">
        <line class="slash-line" x1="-100" y1="110" x2="300" y2="110"/>
        <line class="slash-line" x1="-100" y1="170" x2="300" y2="170"/>
        <line class="slash-line" x1="-100" y1="230" x2="300" y2="230"/>
        <line class="slash-line" x1="-100" y1="290" x2="300" y2="290"/>
        <line class="slash-line" x1="-100" y1="350" x2="300" y2="350"/>
        <rect class="slash-bar" x="0" y="160" width="120" height="11"/>
        <rect class="slash-bar" x="40" y="182" width="130" height="11"/>
        <rect class="slash-bar" x="20" y="208" width="140" height="11"/>
        <rect class="slash-bar" x="60" y="232" width="120" height="11"/>
        <rect class="slash-bar" x="40" y="256" width="130" height="11"/>
      </g>
    </g>
    <rect class="squiggle-field" x="8" y="70" width="44" height="45" role="img" aria-label="Red wavy line pattern"/>
    <rect class="squiggle-field" x="142" y="290" width="46" height="45" role="img" aria-label="Red wavy line pattern"/>
    <text class="site-url" transform="translate(90 327) rotate(-90)" dominant-baseline="central" textLength="232" lengthAdjust="spacing">www.loomferal.co</text>
  </svg>

</main>
</body>
</html>
```